Fahrzeugbeschriftung für Fahrschule
Zielgruppe
Fahrschule für PKW
Aufgabenstellung
Name der Fahrschule, maximal 2 Farben am besten Schwarz und ggf. Rot. (see Logo attached)
Name:
Velmoraq Fahrschule (GmbH) muss nicht drauf sein.
Internet: www.lenkweg-vq.de <- (NOT online yet!)
Daten wie Adresse und Telefonnr. zu finden da (Tel Nr muss drauf sein)
Telenr: 0711 / 48376210
THE LOGO Attached is our Logo but if you can transform it to more like fit for cars we would love it.
Design für Auto gesucht (Golf, Hyundai I30, Mercedes A Klasse - daher ein Generisches Design ausgerichtet für PKW)

```html
<!DOCTYPE html>
<html lang="de">
<head>
<meta charset="utf-8">
<title>Velmoraq Fahrschule – Fahrzeugbeschriftung</title>
<link rel="stylesheet" href="https://fonts.googleapis.com/css2?family=Montserrat:wght@500;600;700&display=swap">
<style>
  :root {
    --paper: #ffffff;
    --ink: #1d1d1f;
    --signal-red: #e3120b;
    --steel: #c9c9cc;
    --type: "Montserrat", Arial, sans-serif;
  }
  html, body {
    margin: 0;
    width: 1200px;
    height: 1200px;
    overflow: hidden;
    background: var(--paper);
  }
  .sheet { display: block; width: 1200px; height: 1200px; }
  .band-red { fill: var(--signal-red); }
  .band-ink { fill: var(--ink); }
  .swoosh-steel { fill: var(--steel); }
  .pinline { stroke: var(--ink); stroke-width: 1.3; fill: none; }
  .label { font-family: var(--type); font-weight: 600; }
  .label-phone { fill: var(--paper); font-size: 10px; font-weight: 700; }
  .label-web { fill: var(--ink); font-size: 9px; }
  .label-address { fill: var(--paper); font-size: 6.4px; }
  .wordmark { fill: var(--paper); font-family: var(--type); font-weight: 700; }
  .wordmark-name { font-size: 17px; }
  .wordmark-sub { font-size: 6.5px; }
  .icon-light { fill: var(--paper); }
</style>
</head>
<body>
<svg class="sheet" viewBox="0 0 1200 1200" xmlns="http://www.w3.org/2000/svg">
  <defs>
    <linearGradient id="dot-fade" x1="0" y1="0" x2="1" y2="0">
      <stop offset="0" stop-color="#1d1d1f" stop-opacity="0.05"/>
      <stop offset="1" stop-color="#1d1d1f" stop-opacity="0.55"/>
    </linearGradient>

    <g id="decal-shapes">
      <!-- halftone field -->
      <path role="img" aria-label="Halbton-Punktraster, nach rechts dichter werdend" fill="url(#dot-fade)"
            d="M158,82 L330,92 Q365,96 385,150 L165,142 Z"/>
      <!-- steel swoosh -->
      <path class="swoosh-steel" d="M150,66 L340,80 Q392,86 432,152 L418,152 Q385,98 332,90 L152,76 Z"/>
      <!-- red swoosh -->
      <path class="band-red" d="M150,58 L345,72 Q398,78 438,152 L424,152 Q388,92 336,84 L154,68 Z"/>
      <!-- logo block -->
      <path class="band-ink" d="M355,73 L652,88 Q606,96 590,132 Q580,158 558,158 L448,158 Q430,112 395,86 Q380,76 355,73 Z"/>
      <!-- top red band -->
      <path class="band-red" d="M0,4 L148,12 Q168,13 178,22 Q186,28 205,30 L644,70 L640,76 L200,40 L20,27 Z"/>
      <!-- black band -->
      <path class="band-ink" d="M14,30 L200,42 L656,82 L652,88 L160,57 L22,47 Z"/>
      <!-- pinlines -->
      <line class="pinline" x1="180" y1="24" x2="322" y2="34"/>
      <line class="pinline" x1="442" y1="43" x2="560" y2="53"/>
    </g>

    <g id="phone-icon">
      <path class="icon-light" d="M1,1 Q0,5 3,9 Q6,12 9,12 L10.5,10 L8,8 L6.8,9 Q4,7 3,4.5 L4,3.3 L2.5,0.5 Z"/>
    </g>
    <g id="pin-icon">
      <path class="icon-light" d="M3,0 A3,3 0 0 1 6,3 Q6,5 3,8 Q0,5 0,3 A3,3 0 0 1 3,0 Z M3,1.8 A1.2,1.2 0 1 0 3,4.2 A1.2,1.2 0 1 0 3,1.8 Z" fill-rule="evenodd"/>
    </g>
  </defs>

  <!-- Decal: driver side -->
  <g class="decal decal-left" transform="translate(56 300) scale(1.65)">
    <use href="#decal-shapes"/>
    <g transform="rotate(3.2 40 16)">
      <use href="#phone-icon" transform="translate(44 8)"/>
      <text class="label label-phone" x="60" y="19">0711 48376210</text>
    </g>
    <text class="label label-web" x="336" y="37" transform="rotate(5 336 37)">www.lenkweg-vq.de</text>
    <g transform="rotate(4 150 50)">
      <use href="#pin-icon" transform="translate(150 44) scale(0.9)"/>
      <text class="label label-address" x="158" y="51">Birkenau Str. 12, 70173 Stuttgart</text>
    </g>
    <text class="wordmark wordmark-name" x="512" y="120" text-anchor="middle">Velmoraq</text>
    <text class="wordmark wordmark-sub" x="512" y="131" text-anchor="middle">Fahrschule</text>
  </g>

  <!-- Decal: passenger side (mirrored artwork, upright type) -->
  <g class="decal decal-right" transform="translate(56 680) scale(1.65)">
    <use href="#decal-shapes" transform="translate(660 0) scale(-1 1)"/>
    <g transform="rotate(-3.2 620 16)">
      <use href="#phone-icon" transform="translate(536 8)"/>
      <text class="label label-phone" x="552" y="19">0711 48376210</text>
    </g>
    <text class="label label-web" x="324" y="37" text-anchor="end" transform="rotate(-5 324 37)">www.lenkweg-vq.de</text>
    <g transform="rotate(-4 510 50)">
      <use href="#pin-icon" transform="translate(391 44) scale(0.9)"/>
      <text class="label label-address" x="399" y="51">Birkenau Str. 12, 70173 Stuttgart</text>
    </g>
    <text class="wordmark wordmark-name" x="148" y="120" text-anchor="middle">Velmoraq</text>
    <text class="wordmark wordmark-sub" x="148" y="131" text-anchor="middle">Fahrschule</text>
  </g>
</svg>
</body>
</html>
```